Business Card Design

The business card is for an IT services company with a specialism
in Integration Services Markets are Health, Government and finance, we provide Velmora SOA platforms and CPB Keystone integration. We are developing multi-agency connectivity

Industry/Entity Type

Business

Contact Information for Business Card

Martin Pell
Director

QVRB Ltd Martin.pell@qvrbltd.example

Mobile: +44 (0) 7700900418
Tel: +44 (0) 1632 960372
Website: www.qvrbltd.example

Ashcombe House, Ashcombe Yard, Melksham SN99 2ZX

Fenwick Harlowe
Health Integration Services

Mobile +44 (0) 07700900527
Tel +44 (0) 1632 960372
Address as above

```html
<!DOCTYPE html>
<html lang="en">
<head>
<meta charset="utf-8">
<title>QVRB Ltd – Business Card</title>
<link rel="stylesheet" href="https://fonts.googleapis.com/css2?family=Arimo:wght@700&family=PT+Sans+Narrow:wght@700&family=Nanum+Gothic&display=swap">
<style>
  :root {
    --ink: #000000;
    --paper: #ffffff;
    --accent: #00ff00;
    --band-fill: #b5fd7a;
    --frame: #000000;
  }
  html, body {
    margin: 0;
    padding: 0;
    width: 1200px;
    height: 899px;
    overflow: hidden;
    background: var(--paper);
  }
  .card {
    position: absolute;
    left: 71px;
    top: 100px;
    width: 1040px;
    height: 685px;
    box-sizing: border-box;
    border: 2px solid var(--frame);
    overflow: hidden;
    color: var(--ink);
  }
  .card-band {
    position: absolute;
    left: 0;
    right: 0;
    bottom: 0;
    height: 135px;
    background: linear-gradient(to bottom, rgba(181, 253, 122, 0) 0%, var(--band-fill) 55%, var(--band-fill) 100%);
  }
  .company-name {
    position: absolute;
    left: 0;
    width: 1048px;
    top: 80px;
    margin: 0;
    text-align: center;
    font-family: "Arimo", Arial, sans-serif;
    font-weight: 700;
    font-size: 62px;
    line-height: 1;
    letter-spacing: -1.5px;
  }
  .rule {
    position: absolute;
    top: 150px;
    height: 18px;
    background: var(--accent);
  }
  .rule-long { left: 0; width: 531px; }
  .rule-short { left: 565px; width: 96px; }
  .person {
    position: absolute;
    left: 0;
    width: 1024px;
    top: 232px;
    text-align: center;
  }
  .person-name {
    margin: 0;
    font-family: "PT Sans Narrow", "Arial Narrow", sans-serif;
    font-weight: 700;
    font-size: 46px;
    line-height: 52px;
  }
  .person-role {
    margin: 0;
    font-family: "Nanum Gothic", Arial, sans-serif;
    font-size: 34px;
    line-height: 40px;
  }
  .contact {
    position: absolute;
    margin: 0;
    font-family: "Nanum Gothic", Arial, sans-serif;
    font-style: normal;
    font-size: 30px;
    line-height: 44px;
    letter-spacing: 0.6px;
    white-space: nowrap;
  }
  .contact-address { left: 75px; top: 414px; }
  .contact-lines { left: 554px; top: 370px; }
</style>
</head>
<body>
  <main class="card">
    <div class="card-band" role="img" aria-label="Soft green decorative band along the bottom of the card"></div>

    <h1 class="company-name">QVRB Ltd</h1>
    <div class="rule rule-long"></div>
    <div class="rule rule-short"></div>

    <section class="person">
      <p class="person-name">Martin Pell</p>
      <p class="person-role">Director</p>
    </section>

    <address class="contact contact-address">
      Ashcombe House,<br>
      Ashcombe Yard,<br>
      Brindlecombe SN99 2ZX
    </address>

    <p class="contact contact-lines">
      martin.pell@qvrbltd.example<br>
      Mobile:+44 (0) 7700900418<br>
      Tel:+44 (0) 1632 960372<br>
      Website:www.qvrbltd.example
    </p>
  </main>
</body>
</html>
```